Verdant Harvest Collective - Business Card Design Project

We need business cards for our business. We grow roots and fruits in Central and South America, we import and distribute in FL, USA. We do fresh and frozen products.

Target Market(s)

Small and big supermarkets, wholesalers, traders, distributors, etc

Industry/Entity Type

Business

```html
<!DOCTYPE html>
<html lang="en">
<head>
<meta charset="utf-8">
<title>Verdant Harvest Collective – Business Cards</title>
<link rel="stylesheet" href="https://fonts.googleapis.com/css2?family=Quicksand:wght@500;600;700&display=swap">
<style>
  :root {
    --backdrop: #2a2a2a;
    --orange: #e8850a;
    --orange-deep: #d9770a;
    --leaf-green: #4f6330;
    --card-white: #f7f7f5;
    --ink-white: #ffffff;
  }
  * { box-sizing: border-box; margin: 0; padding: 0; }
  html, body {
    width: 1200px; height: 997px; overflow: hidden;
    background: var(--backdrop);
    font-family: "Quicksand", sans-serif;
  }
  .card {
    position: absolute;
    width: 560px; height: 320px;
    border-radius: 3px;
    box-shadow: 0 18px 40px rgba(0,0,0,0.55);
  }
  .card--front {
    left: 60px; top: 120px;
    background: var(--orange);
    display: flex; align-items: center; justify-content: center;
  }
  .brand {
    display: flex; align-items: center; gap: 12px;
    font-weight: 700; letter-spacing: 0.5px;
  }
  .brand__dot { width: 14px; height: 14px; border-radius: 50%; }
  .card--front .brand { color: var(--ink-white); font-size: 30px; }
  .card--front .brand__dot { background: var(--ink-white); }

  .card--back { left: 580px; top: 520px; background: var(--card-white); }
  .card--back .brand {
    position: absolute; right: 34px; top: 42px;
    color: var(--orange); font-size: 20px; gap: 8px;
  }
  .card--back .brand__dot { width: 10px; height: 10px; background: var(--orange); }

  .rule {
    position: absolute; left: 190px; right: 34px; top: 160px;
    height: 3px; background: var(--orange-deep);
  }
  .person { position: absolute; left: 30px; top: 143px; }
  .person__name { color: var(--orange); font-size: 21px; font-weight: 600; }
  .person__role { color: var(--leaf-green); font-size: 16px; font-weight: 700; margin-top: 2px; }

  .contacts {
    position: absolute; left: 30px; top: 212px;
    list-style: none;
  }
  .contacts li {
    display: flex; align-items: center; gap: 10px;
    color: var(--leaf-green); font-size: 14px; font-weight: 600;
    height: 23px;
  }
  .contacts svg { width: 15px; height: 15px; fill: var(--orange); flex: none; }

  .address {
    position: absolute; right: 34px; top: 180px;
    color: var(--leaf-green); font-size: 13px; font-weight: 600;
    line-height: 1.55; text-align: right; font-style: normal;
  }
</style>
</head>
<body>
  <section class="card card--front" aria-label="Card front">
    <div class="brand"><span class="brand__dot"></span>Verdant Harvest Collective</div>
  </section>

  <section class="card card--back" aria-label="Card back">
    <div class="brand"><span class="brand__dot"></span>Verdant Harvest Collective</div>
    <div class="rule"></div>
    <div class="person">
      <p class="person__name">Your Name</p>
      <p class="person__role">Director</p>
    </div>
    <ul class="contacts">
      <li>
        <svg viewBox="0 0 16 16" aria-hidden="true"><path d="M2 6c0-2 2-3 6-3s6 1 6 3v1h-3V5.5H5V7H2zM4 8h8l2 5H2z"/></svg>
        0049 155 2870416
      </li>
      <li>
        <svg viewBox="0 0 16 16" aria-hidden="true"><path d="M4 1h8v4H4zM1 6h14v7h-3v2H4v-2H1zM5 10v4h6v-4z"/></svg>
        0049 155 2870422
      </li>
      <li>
        <svg viewBox="0 0 16 16" aria-hidden="true"><path d="M1 3h14v10H1zM2.5 4.5 8 9l5.5-4.5v-.2h-11z" fill-rule="evenodd"/></svg>
        info@verdantharvest.com
      </li>
      <li>
        <svg viewBox="0 0 16 16" aria-hidden="true"><path d="M6.5 9.5 9.5 6.5l1 1-3 3zM4 8 2 10a2.5 2.5 0 0 0 4 4l2-2-1-1-2 2a1 1 0 0 1-2-2l2-2zM12 8l2-2a2.5 2.5 0 0 0-4-4L8 4l1 1 2-2a1 1 0 0 1 2 2l-2 2z"/></svg>
        www.verdantharvest.com
      </li>
    </ul>
    <address class="address">2280 N. Orchard Lane,<br>Palmview, Florida 33910</address>
  </section>
</body>
</html>
```